Buch-/E-Book-Cover für Ratgeber gesucht
Zielgruppe
Es handelt sich um einen Ratgeber zum Thema 'Die Brücke zur Ruhe: Wie du es nun lernst, gelassen zu leben!'.
Das Buch richtet sich vor allem an Frauen im Alter zwischen 18-45 Jahren.
Wie der Titel des Buches bereits aussagt, besteht das Buch aus verschiedenen Kapiteln zum Thema: 'Wie man glücklich wird'.
Aufgabenstellung
*UPDATE: 16.02.2023 / 19:00 Uhr*
Ich habe Beispielcover (1-7) hochgeladen, die ihr als Inspiration für eure Covervorschläge nutzen könnt. Es sollten natürlich keine 1:1 Kopien sein.
Danke!
1.) Der Haupttitel des Buches lautet 'Die Brücke zur Ruhe'
2.) Der Untertitel des Buches lautet 'Wie du es nun lernst, gelassen zu leben!'
3.) Der Name der Autorin lautet 'Lina Hartung'
4.) Der Verlagsname lautet 'deine Morgenstille'.
5.)Das Cover sollte eine Mischung aus 'modern/schlicht' und 'klassisch' sein und nach Möglichkeit Elemente enthalten wie:
- der Hintergrund aus einer Pastellfarbe. Wichtige Elemente können jedoch mit einer Kontrastfarbe hervorgehoben werden
- kein 'eintöniger/einfarbiger' Hintergrund, sondern z. B. mit einem 'Muster'
- Der Haupttitel kann gerne aus verschiedenen Schriftarten bestehen (modern/klassisch) und etwas größer sein, damit er direkt ersichtlich ist.
- aussagekräftige(s) Symbol(e) passend zum Titel ('Die Brücke zur Ruhe').
- Vektorgrafiken/-elemente anstelle von 'Fotos'
6.) Es wird ein Cover für ein Ebook, Taschenbuch als auch Hardcover benötigt.
7.) Das Buch hat ca. 229 Seiten und ein Format von 6x9 Zoll. Die Formatvorlage für Bücherhafen und andere Plattformen kann gerne zu Verfügung gestellt werden.
8.) Ich besitze eine kostenpflichtige Lizenz bei bildmarkt, sodass hier gerne jede Grafik bezogen werden kann. Wenn eine Grafik nur auf einer anderen Plattform vorhanden ist, dann bin ich bereit diese zu kaufen.
9.) Es werden weitere Bücher in dem Themengebiet folgen, sodass eine langfristige Kooperation zum Designen von Covern angedacht ist.

```html
<!DOCTYPE html>
<html lang="de">
<head>
<meta charset="utf-8">
<title>Die Brücke zur Ruhe – Cover</title>
<link rel="stylesheet" href="https://fonts.googleapis.com/css2?family=Playfair+Display+SC:wght@700;900&family=Oswald:wght@600&family=Mulish:wght@300;500&display=swap">
<style>
  :root {
    --paper: #f6f5ee;
    --canvas: #ffffff;
    --gold: #c29a2e;
    --gold-light: #e2c468;
    --ink: #2b2b2b;
    --spine-line: #e6e4d8;
  }
  * { margin: 0; padding: 0; box-sizing: border-box; }
  html, body { width: 894px; height: 1200px; overflow: hidden; background: var(--canvas); }
  .canvas { position: relative; width: 894px; height: 1200px; }

  .title-font { font-family: "Playfair Display SC", Georgia, serif; font-weight: 900; color: var(--gold); text-shadow: 1px 2px 1px rgba(90, 70, 20, 0.35); }
  .author-font { font-family: "Oswald", "Arial Narrow", sans-serif; font-weight: 600; color: var(--gold); }
  .sub-font { font-family: "Mulish", Arial, sans-serif; font-weight: 500; color: var(--gold); }

  /* Print spread */
  .spread { position: absolute; left: 22px; top: 52px; width: 850px; height: 652px; background: var(--paper); box-shadow: 0 0 0 1px #ecebe2; }
  .spine { position: absolute; left: 405px; top: 0; width: 36px; height: 100%; border-left: 1px solid var(--spine-line); border-right: 1px solid var(--spine-line); }

  .back-title { position: absolute; left: 62px; top: 54px; font-size: 31px; line-height: 34px; }
  .back-copy { position: absolute; left: 62px; top: 152px; width: 292px; font-family: "Mulish", Arial, sans-serif; font-weight: 300; font-size: 12px; line-height: 15.1px; color: var(--ink); }
  .publisher { position: absolute; left: 65px; top: 566px; font-family: "Mulish", Arial, sans-serif; font-weight: 500; font-size: 16px; line-height: 20px; color: var(--gold); }

  .spine-title { position: absolute; left: 50%; top: 56px; width: 300px; height: 36px; transform-origin: 0 0; transform: rotate(-90deg) translate(-300px, -18px); font-size: 19px; line-height: 36px; text-align: right; white-space: nowrap; text-shadow: none; }
  .spine-author { position: absolute; left: 50%; top: 503px; width: 96px; height: 36px; transform-origin: 0 0; transform: rotate(-90deg) translate(-96px, -18px); font-size: 19px; line-height: 36px; white-space: nowrap; }

  .front { position: absolute; left: 441px; top: 0; width: 409px; height: 100%; text-align: center; }
  .front .titles { position: absolute; left: 0; right: 0; top: 20px; }
  .front .titles span { display: block; }
  .front .t-small { font-size: 46px; line-height: 56px; }
  .front .t-large { font-size: 66px; line-height: 78px; }
  .front .t-xl { font-size: 82px; line-height: 88px; }
  .front .author { position: absolute; left: 0; right: 0; top: 296px; font-size: 22px; line-height: 30px; }
  .front .art { position: absolute; left: 77px; top: 328px; width: 276px; height: 206px; border-radius: 10px; background: radial-gradient(circle at 40% 50%, var(--gold-light), var(--gold) 55%, rgba(194,154,46,0.15) 80%, transparent); }
  .front .subtitle { position: absolute; left: 0; right: 0; top: 536px; font-size: 19px; line-height: 26px; }

  /* E-book cover */
  .ebook { position: absolute; left: 342px; top: 778px; width: 207px; height: 296px; background: var(--paper); box-shadow: 0 0 0 1px #ecebe2; text-align: center; }
  .ebook .titles { position: absolute; left: 0; right: 0; top: 12px; }
  .ebook .titles span { display: block; }
  .ebook .t-small { font-size: 20px; line-height: 24px; text-shadow: none; }
  .ebook .t-large { font-size: 28px; line-height: 32px; text-shadow: none; }
  .ebook .t-xl { font-size: 34px; line-height: 38px; text-shadow: none; }
  .ebook .author { position: absolute; left: 0; right: 0; top: 141px; font-size: 11px; line-height: 13px; }
  .ebook .art { position: absolute; left: 28px; top: 156px; width: 136px; height: 100px; border-radius: 6px; background: radial-gradient(circle at 40% 50%, var(--gold-light), var(--gold) 55%, rgba(194,154,46,0.15) 80%, transparent); }
  .ebook .subtitle { position: absolute; left: 0; right: 0; top: 256px; font-size: 9.5px; line-height: 12px; }
</style>
</head>
<body>
<div class="canvas">

  <section class="spread">
    <div class="back">
      <h2 class="back-title title-font">Die Brücke<br>zur Ruhe</h2>
      <p class="back-copy">
        Wie werde ich gelassen?<br>
        Diese Frage ist mindestens genauso so alt wie die Menschheit selbst. Doch was, wenn uns nur eine einzige Brücke fehlt, um den Weg zur Ruhe zu gehen? Wir gehen hinaus in die weite Welt und suchen die Ruhe überall - nur nicht dort, wo sie am offensichtlichsten ist. Alles wonach du suchst, steckt bereits in dir, du musst nur den richtigen Weg gehen.<br>
        Mit diesem Buch möchte ich dich auf eine Reise mitnehmen, um gemeinsam mit dir die Brücke zur Ruhe zu finden für ein Leben voller Erfüllung und Dankbarkeit!<br>
        Zudem wirst du lernen, wie du ...<br>
        ... einen felsenfesten Glauben in dich Selbst entwickelst, der es dir ermöglicht, deinen Selbstwert zu erkennen.<br>
        ... geduldig an deinen Zielen festhältst, ganz egal welches Hindernis deinen Träumen im Weg stehen mag.<br>
        ...alle Dinge loslässt, die dich davon abhalten, ein Leben nach deinen Vorstellungen zu leben.<br>
        ... deine größten Ängste überwindest, um in all deinen Lebensbereichen bedingungslose Liebe zu verkörpern.<br>
        ... durch die Macht der Dankbarkeit, deine persönliche Ruhe findest und sie für immer behältst.
      </p>
      <p class="publisher">deine Morgenstille</p>
    </div>

    <div class="spine">
      <p class="spine-title title-font">Die Brücke zur Ruhe</p>
      <p class="spine-author author-font">Lina Hartung</p>
    </div>

    <div class="front">
      <h1 class="titles title-font">
        <span class="t-small">Die</span>
        <span class="t-large">Brücke</span>
        <span class="t-small">zur</span>
        <span class="t-xl">Ruhe</span>
      </h1>
      <p class="author author-font">Lina Hartung</p>
      <div class="art" role="img" aria-label="Goldene Illustration: verziertes Herzschloss mit passendem Schlüssel"></div>
      <p class="subtitle sub-font">Wie du es<br>nun lernst,<br>gelassen zu leben!</p>
    </div>
  </section>

  <section class="ebook">
    <h1 class="titles title-font">
      <span class="t-small">Die</span>
      <span class="t-large">Brücke</span>
      <span class="t-small">zur</span>
      <span class="t-xl">Ruhe</span>
    </h1>
    <p class="author author-font">Lina Hartung</p>
    <div class="art" role="img" aria-label="Goldene Illustration: verziertes Herzschloss mit passendem Schlüssel"></div>
    <p class="subtitle sub-font">Wie du es<br>nun lernst,<br>gelassen zu leben!</p>
  </section>

</div>
</body>
</html>
```